Tallow Bright business card

Tallow Bright is a new online life insurance company providing instant quotes and policies to consumers.
Target Market(s)
Target market is both business to business as well as business to consumer
Can think out side of the box- We are an open minded bunch
Industry/Entity Type
Life Insurance
Requirements
Must have
- Our corporate Logo
Double sided
Website www.tallowbright.com.au
Phone Number
Name & Position of each person etc.
Modern font

```html
<!DOCTYPE html>
<html lang="en">
<head>
<meta charset="utf-8">
<title>Tallow Bright – Business Card</title>
<link rel="stylesheet" href="https://fonts.googleapis.com/css2?family=Jura:wght@500;600&display=swap">
<style>
  :root {
    --ink: #1c1c1c;
    --brand-ink: #262626;
    --brand-soft: #8a8a8a;
    --accent: #f08a24;
    --paper: #ffffff;
    --backdrop: #ffffff;
    --card-shadow: rgba(0, 0, 0, 0.35);
  }
  * { box-sizing: border-box; margin: 0; padding: 0; }
  html, body {
    width: 1200px; height: 1200px; overflow: hidden;
    background: var(--backdrop);
  }
  body { position: relative; font-family: "Jura", sans-serif; color: var(--ink); }

  .card {
    position: absolute;
    width: 870px; height: 565px;
    background: var(--paper);
    overflow: hidden;
    box-shadow: 2px 3px 4px var(--card-shadow);
  }
  .card--front { left: 0; top: 0; }
  .card--back { left: 330px; top: 620px; }

  .card__wave { position: absolute; inset: 0; width: 100%; height: 100%; }

  .brand {
    position: absolute;
    display: flex; align-items: center; gap: 14px;
    font-weight: 600; letter-spacing: -1px; white-space: nowrap;
  }
  .brand__dot { border-radius: 50%; background: var(--accent); flex: none; }
  .card--front .brand { left: 62px; top: 58px; font-size: 72px; color: var(--brand-ink); }
  .card--front .brand__dot { width: 22px; height: 22px; }
  .card--back .brand { left: 300px; top: 112px; font-size: 38px; color: var(--brand-soft); gap: 9px; }
  .card--back .brand__dot { width: 12px; height: 12px; }

  .person { position: absolute; left: 430px; top: 300px; width: 356px; text-align: center; }
  .person__name { font-size: 40px; font-weight: 600; letter-spacing: -0.5px; }
  .person__title { font-size: 24px; font-weight: 600; margin-top: 4px; }

  .contact { position: absolute; left: 435px; top: 428px; font-size: 32px; font-weight: 600; line-height: 48px; letter-spacing: -0.5px; }

  .details { position: absolute; left: 190px; top: 310px; font-size: 30px; font-weight: 600; line-height: 52px; letter-spacing: -0.3px; }
  .details__address { margin-top: 22px; }
  .details__indent { padding-left: 70px; }
</style>
</head>
<body>

<section class="card card--front" aria-label="Card front">
  <svg class="card__wave" viewBox="0 0 870 565" aria-hidden="true">
    <defs>
      <linearGradient id="glowFront" x1="0" y1="0" x2="0" y2="1">
        <stop offset="0" stop-color="#fff8d8" stop-opacity="0"/>
        <stop offset="0.45" stop-color="#fde9a2"/>
        <stop offset="0.8" stop-color="#f6cf80"/>
        <stop offset="1" stop-color="#d9a07e"/>
      </linearGradient>
      <filter id="softFront" x="-10%" y="-30%" width="120%" height="160%">
        <feGaussianBlur stdDeviation="14"/>
      </filter>
      <filter id="edgeFront"><feGaussianBlur stdDeviation="3"/></filter>
    </defs>
    <path d="M-40 140 C 200 150, 500 190, 910 200 L 910 330 C 800 330, 760 300, 720 262 C 660 220, 580 240, 470 270 C 330 310, 160 330, -40 280 Z"
          fill="url(#glowFront)" filter="url(#softFront)"/>
    <path d="M-40 290 C 160 335, 330 318, 470 280 C 580 250, 655 228, 712 268 C 760 305, 800 326, 910 322 L 910 600 L -40 600 Z"
          fill="#ffffff" filter="url(#edgeFront)"/>
  </svg>

  <div class="brand"><span class="brand__name">Tallow Bright</span><span class="brand__dot"></span></div>

  <div class="person">
    <p class="person__name">Full Name</p>
    <p class="person__title">Job Title</p>
  </div>

  <div class="contact">
    <p class="contact__email">email: email:email:email</p>
    <p class="contact__phone">phone: 1300 555 019</p>
  </div>
</section>

<section class="card card--back" aria-label="Card back">
  <svg class="card__wave" viewBox="0 0 870 565" aria-hidden="true">
    <defs>
      <linearGradient id="glowBack" x1="0" y1="0" x2="0" y2="1">
        <stop offset="0" stop-color="#fff8e0" stop-opacity="0"/>
        <stop offset="0.5" stop-color="#fdeab0"/>
        <stop offset="0.85" stop-color="#f5d08c"/>
        <stop offset="1" stop-color="#e0b090"/>
      </linearGradient>
      <filter id="softBack" x="-10%" y="-30%" width="120%" height="160%">
        <feGaussianBlur stdDeviation="16"/>
      </filter>
      <filter id="edgeBack"><feGaussianBlur stdDeviation="3"/></filter>
    </defs>
    <path d="M-40 20 C 250 40, 600 30, 910 -10 L 910 120 C 820 170, 720 230, 560 250 C 400 270, 300 250, 230 300 C 170 350, 80 360, -40 350 Z"
          fill="url(#glowBack)" filter="url(#softBack)"/>
    <path d="M-40 360 C 90 372, 175 350, 238 305 C 300 262, 400 278, 560 262 C 720 245, 820 180, 910 128 L 910 600 L -40 600 Z"
          fill="#ffffff" filter="url(#edgeBack)"/>
  </svg>

  <div class="brand"><span class="brand__name">Tallow Bright</span><span class="brand__dot"></span></div>

  <div class="details">
    <p class="details__web">www.tallowbright.com.au</p>
    <p class="details__address">Address: Level 9, 45 Harbour Lane</p>
    <p class="details__indent">Eastwood NSW 2122</p>
  </div>
</section>

</body>
</html>
```